social interest sharing site needs a web site design

we need a web site design for a social web platform.
the site is one page(main page), that is split into 3 sections
each section is a different color(red,green and blue)
and a user can choose to share each of the sections.
any section/color will contain boxes , each box can contain different media types.

the media types:
* list of URLS
* list of articles including title + image + description
* list of videos
* thumbnails of images
* calender
* list of emails

the main content will look like corkboardly layout
multiple boxes each box can contain different type of content as described above

each color is a different tab
each tab will have layout like corkboardly
Updates

please read the last description update.
and i uploaded an image that can explain the requirements better

thanks
Oren
 

Industry/Entity Type

Media

```html
<!DOCTYPE html>
<html lang="en">
<head>
<meta charset="utf-8">
<title>Hueboard</title>
<link rel="stylesheet" href="https://fonts.googleapis.com/css2?family=Oswald:wght@600;700&family=Open+Sans:wght@400;700&display=swap">
<style>
:root{
  --ink:#1b1b1b;
  --red:#cf0b0b;
  --green:#1f8a2f;
  --blue:#2563ae;
  --white:#ffffff;
  --panel-line:#b9b9b9;
  --track:#d8d8d8;
  --thumb:#8a8a8a;
  --cal-bg:#111111;
  --cal-cell:#e9e9e9;
  --photo-a:#e9d2bd;
  --photo-b:#b9a48f;
}
*{box-sizing:border-box;margin:0;padding:0}
html,body{width:717px;height:1200px;overflow:hidden}
body{font-family:"Open Sans",Arial,sans-serif;color:var(--white);background:var(--ink)}
.site-header{height:30px;background:var(--ink);padding-left:48px;display:flex;align-items:center}
.brand{font-family:"Oswald",Arial,sans-serif;font-weight:700;font-size:21px;letter-spacing:1px;color:var(--white)}
.board{position:relative;height:378px}
.board--red{background:var(--red)}
.board--green{background:var(--green)}
.board--blue{background:var(--blue)}
.picker{position:absolute;top:14px;height:12px;width:144px;background:var(--white);border:1px solid #999;color:#333;font-size:6px;line-height:10px;padding-left:4px}
.picker::after{content:"";position:absolute;right:4px;top:3px;border:3px solid transparent;border-top-color:#555}
.picker--one{left:210px}
.picker--two{left:359px}
.box-title{position:absolute;font-weight:700;font-size:14px}
.box-title--videos{left:120px;top:34px}
.box-title--images{left:370px;top:34px}
.box-title--articles{left:120px;top:214px}
.media-panel{position:absolute;top:54px;height:142px;background:var(--white);border:1px solid var(--panel-line);padding:6px 6px 16px}
.media-panel--videos{left:120px;width:238px}
.media-panel--images{left:370px;width:256px}
.thumb-grid{display:grid;grid-template-columns:repeat(4,1fr);grid-template-rows:repeat(3,1fr);gap:4px;height:100%}
.thumb{background:linear-gradient(160deg,var(--photo-a),var(--photo-b));border:1px solid #ddd}
.scrollbar{position:absolute;left:8px;right:8px;bottom:5px;height:5px;background:var(--track);border-radius:3px}
.scrollbar span{position:absolute;left:0;top:0;height:5px;width:40%;background:var(--thumb);border-radius:3px}
.pager{position:absolute;left:592px;top:216px;width:34px;height:12px}
.article-list{position:absolute;left:120px;top:236px;width:330px}
.article{display:flex;gap:8px;margin-bottom:8px}
.article-photo{flex:0 0 34px;height:30px;border:2px solid var(--white);background:linear-gradient(160deg,var(--photo-a),var(--photo-b))}
.article-title{font-weight:700;font-size:6.5px;line-height:9px}
.article-text{font-size:6px;line-height:8px}
.calendar{position:absolute;left:460px;top:232px;width:166px;background:var(--cal-bg);padding:2px;font-size:6.5px}
.calendar-month{background:var(--red);text-align:center;font-weight:700;line-height:10px}
.calendar table{width:100%;border-collapse:separate;border-spacing:1px}
.calendar th{color:var(--white);font-weight:700;line-height:10px}
.calendar td{background:var(--cal-cell);color:#222;text-align:center;line-height:11px}
.site-footer{height:36px;background:var(--ink);text-align:center;font-size:7px;line-height:36px;color:#bbb}
</style>
</head>
<body>
<header class="site-header"><span class="brand">HUEBOARD</span></header>

<section class="board board--red">
  <div class="picker picker--one">List of Urls</div>
  <div class="picker picker--two">List of Emails</div>
  <h2 class="box-title box-title--videos">List of Videos</h2>
  <h2 class="box-title box-title--images">List of Images</h2>
  <div class="media-panel media-panel--videos"><div class="thumb-grid">
    <div class="thumb" role="img" aria-label="Video thumbnail"></div><div class="thumb" role="img" aria-label="Video thumbnail"></div><div class="thumb" role="img" aria-label="Video thumbnail"></div><div class="thumb" role="img" aria-label="Video thumbnail"></div>
    <div class="thumb" role="img" aria-label="Video thumbnail"></div><div class="thumb" role="img" aria-label="Video thumbnail"></div><div class="thumb" role="img" aria-label="Video thumbnail"></div><div class="thumb" role="img" aria-label="Video thumbnail"></div>
    <div class="thumb" role="img" aria-label="Video thumbnail"></div><div class="thumb" role="img" aria-label="Video thumbnail"></div><div class="thumb" role="img" aria-label="Video thumbnail"></div><div class="thumb" role="img" aria-label="Video thumbnail"></div>
  </div><div class="scrollbar"><span></span></div></div>
  <div class="media-panel media-panel--images"><div class="thumb-grid">
    <div class="thumb" role="img" aria-label="Image thumbnail"></div><div class="thumb" role="img" aria-label="Image thumbnail"></div><div class="thumb" role="img" aria-label="Image thumbnail"></div><div class="thumb" role="img" aria-label="Image thumbnail"></div>
    <div class="thumb" role="img" aria-label="Image thumbnail"></div><div class="thumb" role="img" aria-label="Image thumbnail"></div><div class="thumb" role="img" aria-label="Image thumbnail"></div><div class="thumb" role="img" aria-label="Image thumbnail"></div>
    <div class="thumb" role="img" aria-label="Image thumbnail"></div><div class="thumb" role="img" aria-label="Image thumbnail"></div><div class="thumb" role="img" aria-label="Image thumbnail"></div><div class="thumb" role="img" aria-label="Image thumbnail"></div>
  </div><div class="scrollbar"><span></span></div></div>
  <h2 class="box-title box-title--articles">Latest Articles</h2>
  <svg class="pager" viewBox="0 0 34 12" aria-label="Previous and next"><path d="M7 1 2 6l5 5M27 1l5 5-5 5" fill="none" stroke="#fff" stroke-width="2"/></svg>
  <div class="article-list">
    <article class="article"><div class="article-photo" role="img" aria-label="Article photo"></div><div><h3 class="article-title">Lorem ipsum dolor sit amet, consectetuer adipiscing elit, sed diam nonummy nibh</h3><p class="article-text">Ut wisi enim ad minim veniam, quis nostrud exerci tation ullamcorper suscipit lobortis nisl ut aliquip ex ea commodo consequat duis autem vel eum iriure dolor in hendrerit.</p></div></article>
    <article class="article"><div class="article-photo" role="img" aria-label="Article photo"></div><div><h3 class="article-title">Lorem ipsum dolor sit amet, consectetuer adipiscing elit, sed diam nonummy nibh</h3><p class="article-text">Ut wisi enim ad minim veniam, quis nostrud exerci tation ullamcorper suscipit lobortis nisl ut aliquip ex ea commodo consequat duis autem vel eum iriure dolor in hendrerit.</p></div></article>
  </div>
  <div class="calendar"><div class="calendar-month">DECEMBER 2013</div><table>
    <tr><th>MO</th><th>TU</th><th>WE</th><th>TH</th><th>FR</th><th>SA</th><th>SU</th></tr>
    <tr><td>2</td><td>3</td><td>4</td><td>5</td><td>6</td><td>7</td><td>8</td></tr>
    <tr><td>9</td><td>10</td><td>11</td><td>12</td><td>13</td><td>14</td><td>15</td></tr>
    <tr><td>16</td><td>17</td><td>18</td><td>19</td><td>20</td><td>21</td><td>22</td></tr>
    <tr><td>23</td><td>24</td><td>25</td><td>26</td><td>27</td><td>28</td><td>29</td></tr>
    <tr><td>30</td><td>31</td><td>1</td><td>2</td><td>3</td><td>4</td><td>5</td></tr>
  </table></div>
</section>

<section class="board board--green">
  <div class="picker picker--one">List of Urls</div>
  <div class="picker picker--two">List of Emails</div>
  <h2 class="box-title box-title--videos">List of Videos</h2>
  <h2 class="box-title box-title--images">List of Images</h2>
  <div class="media-panel media-panel--videos"><div class="thumb-grid">
    <div class="thumb" role="img" aria-label="Video thumbnail"></div><div class="thumb" role="img" aria-label="Video thumbnail"></div><div class="thumb" role="img" aria-label="Video thumbnail"></div><div class="thumb" role="img" aria-label="Video thumbnail"></div>
    <div class="thumb" role="img" aria-label="Video thumbnail"></div><div class="thumb" role="img" aria-label="Video thumbnail"></div><div class="thumb" role="img" aria-label="Video thumbnail"></div><div class="thumb" role="img" aria-label="Video thumbnail"></div>
    <div class="thumb" role="img" aria-label="Video thumbnail"></div><div class="thumb" role="img" aria-label="Video thumbnail"></div><div class="thumb" role="img" aria-label="Video thumbnail"></div><div class="thumb" role="img" aria-label="Video thumbnail"></div>
  </div><div class="scrollbar"><span></span></div></div>
  <div class="media-panel media-panel--images"><div class="thumb-grid">
    <div class="thumb" role="img" aria-label="Image thumbnail"></div><div class="thumb" role="img" aria-label="Image thumbnail"></div><div class="thumb" role="img" aria-label="Image thumbnail"></div><div class="thumb" role="img" aria-label="Image thumbnail"></div>
    <div class="thumb" role="img" aria-label="Image thumbnail"></div><div class="thumb" role="img" aria-label="Image thumbnail"></div><div class="thumb" role="img" aria-label="Image thumbnail"></div><div class="thumb" role="img" aria-label="Image thumbnail"></div>
    <div class="thumb" role="img" aria-label="Image thumbnail"></div><div class="thumb" role="img" aria-label="Image thumbnail"></div><div class="thumb" role="img" aria-label="Image thumbnail"></div><div class="thumb" role="img" aria-label="Image thumbnail"></div>
  </div><div class="scrollbar"><span></span></div></div>
  <h2 class="box-title box-title--articles">Latest Articles</h2>
  <svg class="pager" viewBox="0 0 34 12" aria-label="Previous and next"><path d="M7 1 2 6l5 5M27 1l5 5-5 5" fill="none" stroke="#fff" stroke-width="2"/></svg>
  <div class="article-list">
    <article class="article"><div class="article-photo" role="img" aria-label="Article photo"></div><div><h3 class="article-title">Lorem ipsum dolor sit amet, consectetuer adipiscing elit, sed diam nonummy nibh</h3><p class="article-text">Ut wisi enim ad minim veniam, quis nostrud exerci tation ullamcorper suscipit lobortis nisl ut aliquip ex ea commodo consequat duis autem vel eum iriure dolor in hendrerit.</p></div></article>
    <article class="article"><div class="article-photo" role="img" aria-label="Article photo"></div><div><h3 class="article-title">Lorem ipsum dolor sit amet, consectetuer adipiscing elit, sed diam nonummy nibh</h3><p class="article-text">Ut wisi enim ad minim veniam, quis nostrud exerci tation ullamcorper suscipit lobortis nisl ut aliquip ex ea commodo consequat duis autem vel eum iriure dolor in hendrerit.</p></div></article>
  </div>
  <div class="calendar"><div class="calendar-month">DECEMBER 2013</div><table>
    <tr><th>MO</th><th>TU</th><th>WE</th><th>TH</th><th>FR</th><th>SA</th><th>SU</th></tr>
    <tr><td>2</td><td>3</td><td>4</td><td>5</td><td>6</td><td>7</td><td>8</td></tr>
    <tr><td>9</td><td>10</td><td>11</td><td>12</td><td>13</td><td>14</td><td>15</td></tr>
    <tr><td>16</td><td>17</td><td>18</td><td>19</td><td>20</td><td>21</td><td>22</td></tr>
    <tr><td>23</td><td>24</td><td>25</td><td>26</td><td>27</td><td>28</td><td>29</td></tr>
    <tr><td>30</td><td>31</td><td>1</td><td>2</td><td>3</td><td>4</td><td>5</td></tr>
  </table></div>
</section>

<section class="board board--blue">
  <div class="picker picker--one">List of Urls</div>
  <div class="picker picker--two">List of Emails</div>
  <h2 class="box-title box-title--videos">List of Videos</h2>
  <h2 class="box-title box-title--images">List of Images</h2>
  <div class="media-panel media-panel--videos"><div class="thumb-grid">
    <div class="thumb" role="img" aria-label="Video thumbnail"></div><div class="thumb" role="img" aria-label="Video thumbnail"></div><div class="thumb" role="img" aria-label="Video thumbnail"></div><div class="thumb" role="img" aria-label="Video thumbnail"></div>
    <div class="thumb" role="img" aria-label="Video thumbnail"></div><div class="thumb" role="img" aria-label="Video thumbnail"></div><div class="thumb" role="img" aria-label="Video thumbnail"></div><div class="thumb" role="img" aria-label="Video thumbnail"></div>
    <div class="thumb" role="img" aria-label="Video thumbnail"></div><div class="thumb" role="img" aria-label="Video thumbnail"></div><div class="thumb" role="img" aria-label="Video thumbnail"></div><div class="thumb" role="img" aria-label="Video thumbnail"></div>
  </div><div class="scrollbar"><span></span></div></div>
  <div class="media-panel media-panel--images"><div class="thumb-grid">
    <div class="thumb" role="img" aria-label="Image thumbnail"></div><div class="thumb" role="img" aria-label="Image thumbnail"></div><div class="thumb" role="img" aria-label="Image thumbnail"></div><div class="thumb" role="img" aria-label="Image thumbnail"></div>
    <div class="thumb" role="img" aria-label="Image thumbnail"></div><div class="thumb" role="img" aria-label="Image thumbnail"></div><div class="thumb" role="img" aria-label="Image thumbnail"></div><div class="thumb" role="img" aria-label="Image thumbnail"></div>
    <div class="thumb" role="img" aria-label="Image thumbnail"></div><div class="thumb" role="img" aria-label="Image thumbnail"></div><div class="thumb" role="img" aria-label="Image thumbnail"></div><div class="thumb" role="img" aria-label="Image thumbnail"></div>
  </div><div class="scrollbar"><span></span></div></div>
  <h2 class="box-title box-title--articles">Latest Articles</h2>
  <svg class="pager" viewBox="0 0 34 12" aria-label="Previous and next"><path d="M7 1 2 6l5 5M27 1l5 5-5 5" fill="none" stroke="#fff" stroke-width="2"/></svg>
  <div class="article-list">
    <article class="article"><div class="article-photo" role="img" aria-label="Article photo"></div><div><h3 class="article-title">Lorem ipsum dolor sit amet, consectetuer adipiscing elit, sed diam nonummy nibh</h3><p class="article-text">Ut wisi enim ad minim veniam, quis nostrud exerci tation ullamcorper suscipit lobortis nisl ut aliquip ex ea commodo consequat duis autem vel eum iriure dolor in hendrerit.</p></div></article>
    <article class="article"><div class="article-photo" role="img" aria-label="Article photo"></div><div><h3 class="article-title">Lorem ipsum dolor sit amet, consectetuer adipiscing elit, sed diam nonummy nibh</h3><p class="article-text">Ut wisi enim ad minim veniam, quis nostrud exerci tation ullamcorper suscipit lobortis nisl ut aliquip ex ea commodo consequat duis autem vel eum iriure dolor in hendrerit.</p></div></article>
  </div>
  <div class="calendar"><div class="calendar-month">DECEMBER 2013</div><table>
    <tr><th>MO</th><th>TU</th><th>WE</th><th>TH</th><th>FR</th><th>SA</th><th>SU</th></tr>
    <tr><td>2</td><td>3</td><td>4</td><td>5</td><td>6</td><td>7</td><td>8</td></tr>
    <tr><td>9</td><td>10</td><td>11</td><td>12</td><td>13</td><td>14</td><td>15</td></tr>
    <tr><td>16</td><td>17</td><td>18</td><td>19</td><td>20</td><td>21</td><td>22</td></tr>
    <tr><td>23</td><td>24</td><td>25</td><td>26</td><td>27</td><td>28</td><td>29</td></tr>
    <tr><td>30</td><td>31</td><td>1</td><td>2</td><td>3</td><td>4</td><td>5</td></tr>
  </table></div>
</section>

<footer class="site-footer">© 2013 hueboard. All Rights Reserved</footer>
</body>
</html>
```